Training Program Flyers

***Please note an update - the flyers should have somewhere a space that can include a special offer, which can be removed if not applicable with no impact to the design. Have uploaded a graphic of a current example of an offer**

We require 2 flyers to be re-designed which will include:
- Program Flyer
- Training calendar

Current flyers are attached - which are generally 2 pages long.

Program flyers
The newly designed flyer templates should cater for future use across multiple courses and have space for pictures that will be relevant to the content and also allow for additional content to be added if required (ie the template could be extended to a 3rd page)

Training Calendar
This flyer should be flexible to add additional courses as they arise and extend onto further pages easily.

Our branding guidelines and corporate colours should also be followed as attached.

We require editable files in photoshop/illustrator and PDF
The flyers should be A4 in size

Thank you for your time
Corinne

Target Market(s)

Students paying for services

Industry/Entity Type

Training

Font styles to use
Other font styles liked:
• As per brand guidelines

Requirements
Must have
• Corporate Brand Look and Feel

```html
<!DOCTYPE html>
<html lang="en">
<head>
<meta charset="utf-8">
<title>Program Flyer – Course Title</title>
<link href="https://fonts.googleapis.com/css2?family=Arimo:wght@400;700&family=Source+Sans+3:wght@400;600;700&display=swap" rel="stylesheet">
<style>
  :root {
    --brand-blue: #1a72b0;
    --brand-yellow: #fdba13;
    --accent-orange: #f47c20;
    --offer-red: #d2232a;
    --ink: #1d1d1b;
    --paper: #ffffff;
    --star-peach: #f9c3a0;
    --star-light: #fde9a6;
  }
  * { margin: 0; padding: 0; box-sizing: border-box; }
  html, body { width: 848px; height: 1200px; overflow: hidden; background: var(--paper); }
  .flyer {
    position: relative;
    width: 848px;
    height: 1200px;
    overflow: hidden;
    background: var(--paper);
    font-family: "Arimo", Arial, sans-serif;
    color: var(--ink);
  }

  /* Brand block */
  .brand { position: absolute; left: 40px; top: 104px; }
  .brand-name {
    font-family: "Source Sans 3", Arial, sans-serif;
    font-weight: 600; font-size: 50px; line-height: 1;
    color: var(--brand-blue); letter-spacing: -0.5px;
  }
  .brand-tagline {
    margin-top: 6px;
    font-family: "Source Sans 3", Arial, sans-serif;
    font-weight: 600; font-size: 12.5px; letter-spacing: 0.6px; color: var(--brand-blue);
  }

  /* Header bands */
  .header-bands { position: absolute; left: 0; top: 215px; width: 848px; height: 68px; }
  .header-title, .course-title { position: absolute; right: 40px; text-align: right; line-height: 1; }
  .header-title { top: 221px; font-size: 20px; font-weight: 700; color: var(--paper); letter-spacing: 0.5px; }
  .course-title { top: 258px; font-size: 17px; font-weight: 400; color: var(--ink); }

  /* Content sections */
  .section { position: absolute; left: 0; width: 848px; }
  .section-photo { position: absolute; left: 41px; width: 201px; height: 150px; }
  .photo-people { background: linear-gradient(100deg, #c9281f 0%, #d23a2c 45%, #3a3c40 80%, #b12820 100%); }
  .photo-seating { background: linear-gradient(160deg, #e9ebee 0%, #cfd3d8 45%, #c98a3f 70%, #6e8fb8 100%); }
  .section-text { position: absolute; left: 258px; width: 548px; font-size: 14.6px; line-height: 20px; }
  .section-text p + p { margin-top: 11px; }
  .subheader {
    position: absolute; right: 40px; line-height: 1;
    font-size: 20px; font-weight: 700; color: var(--accent-orange); letter-spacing: 0.3px;
  }

  /* Offer */
  .decor-shape {
    position: absolute; left: -70px; top: 930px; width: 320px; height: 320px; border-radius: 50%;
    background: radial-gradient(circle at 50% 50%, var(--star-light) 0%, var(--star-peach) 60%, #fbd3b8 100%);
    opacity: 0.85;
  }
  .offer {
    position: absolute; left: 296px; top: 962px; width: 320px; text-align: center;
    font-family: "Source Sans 3", Arial, sans-serif;
  }
  .offer-amount { font-size: 52px; font-weight: 700; color: var(--offer-red); line-height: 1; letter-spacing: 0.5px; }
  .offer-name { margin-top: 6px; font-size: 31px; font-weight: 700; color: var(--brand-blue); line-height: 1.1; }
  .offer-terms { margin-top: 4px; font-size: 19px; line-height: 22px; }
  .offer-date { font-size: 34px; line-height: 38px; }
  .offer-illustration {
    position: absolute; left: 592px; top: 965px; width: 218px; height: 150px;
    border-radius: 50% 45% 40% 50%;
    background: linear-gradient(160deg, #2f86c6 0%, var(--brand-blue) 60%, #5fa2d6 100%);
  }
</style>
</head>
<body>
<main class="flyer">

  <header>
    <div class="brand">
      <div class="brand-name">quillenby</div>
      <div class="brand-tagline">CAREER SKILLS &amp; PLACEMENT</div>
    </div>

    <svg class="header-bands" viewBox="0 0 848 68" aria-hidden="true">
      <polygon points="148,0 848,0 848,32 177,32" fill="var(--brand-blue)"/>
      <polygon points="185,36 848,36 848,67 148,67" fill="var(--brand-yellow)"/>
    </svg>
    <h1 class="header-title">HEADER ONE</h1>
    <h2 class="course-title">COURSE TITLE</h2>
  </header>

  <section class="section" style="top:319px;">
    <div class="section-photo photo-people" style="top:27px;" role="img" aria-label="Photo of three graduates standing together at a ceremony"></div>
    <div class="section-text">
      <p>Ga. Eveni illaut et es dolore as cori vent atusame cus re qui conetus quossi te pa simos dolupta ssunto quodis eum que arumquam rem suntior ab ilis et a delecte mpelitias est, verit, alicien dignias quisi que dolupta quia des ut mollaborem aut labo. Nam, comnisquiam, simenisitem et et rerat am aspienim et ut apici solor a sit dem non reperiti omnist veliquam qui vel eaquam, volor sum voluptiis aute volor aut erepudignis etur molorerae quis etus volorem con pereror eprerorem as ex evel ius.</p>
      <p>Laborem porerrunt etus dellantia apientibus delluptae voluptatia corit, nim laboribusa volest aut fugia eossece ptatem landusti sequia natur aut rem id qui con renimus volorep erchill upidust ilicidunte sintis nati consequodit dolupiet faccum sunt et esed quos dunt.</p>
    </div>
  </section>

  <h3 class="subheader" style="top:574px;">SUBHEADER</h3>

  <section class="section" style="top:607px;">
    <div class="section-photo photo-seating" style="top:29px;" role="img" aria-label="Photo of a lecture room with rows of colourful tiered seats"></div>
    <div class="section-text">
      <p>Ga. Eveni illaut et es dolore as cori vent atusame cus re qui conetus quossi te pa simos dolupta ssunto quodis eum que arumquam rem suntior ab ilis et a delecte mpelitias est, verit, alicien dignias quisi que dolupta quia des ut mollaborem aut labo. Nam, comnisquiam, simenisitem et et rerat am aspienim et ut apici solor a sit dem non reperiti omnist veliquam qui vel eaquam, volor sum voluptiis aute volor aut erepudignis etur molorerae quis etus volorem con pereror eprerorem as ex evel ius.</p>
      <p>Laborem porerrunt etus dellantia apientibus delluptae voluptatia corit, nim laboribusa volest aut fugia eossece ptatem landusti sequia natur aut rem id qui con renimus volorep erchill upidust ilicidunte sintis nati consequodit dolupiet faccum sunt et esed quos dunt.</p>
    </div>
  </section>

  <div class="decor-shape" role="img" aria-label="Large soft decorative shape in peach and pale yellow"></div>

  <aside class="offer">
    <div class="offer-amount">SAVE $100</div>
    <div class="offer-name">Early Bird Special</div>
    <div class="offer-terms">Students who enrol &amp;<br>pay their deposit by</div>
    <div class="offer-date">22nd December</div>
  </aside>
  <div class="offer-illustration" role="img" aria-label="Illustration of a blue bird in flight"></div>

</main>
</body>
</html>
```